Create for us a Shop-Stopper Business Card

We need a standout, first class business card to go along with our new brand strategy. Sleek, Contemporary and fresh.

Colors and theme must sync with our websitewww.pelvorpower.co.uk

We want a business card that has a global brand appeal. TKR Energy is a small UK renewable company that specialises in energy projects in Africa. We want a business card that has the following characteristics: Very short, precise, global, stand out, NOT TOO LOUD but contemporary. The company's colour themes are White, Grey with a hint of green.

Target Market(s)

Business exec, high net worth individuals, investors, commercial leaders, suppliers, government officials

Industry/Entity Type

Solar Energy

Contact Information for Business Card

Logo, Name, Title, Address, web address, email,

Requirements
Must have
• Logo must be sharp
Nice to have
• Adapt fonts from the logo. The large circular side of the logo at the back in a very refreshing way
Should not have
• No solar panel shapes or image.Very little black. If possible avoid black. Its not coming out nice. I think !!!

```html
<!DOCTYPE html>
<html lang="en">
<head>
<meta charset="utf-8">
<title>TKR Energy – Business Card</title>
<link href="https://fonts.googleapis.com/css2?family=Open+Sans:wght@400;600;700&display=swap" rel="stylesheet">
<style>
  :root {
    --bg: #ecebe8;
    --card-white: #f7f7f7;
    --green-dark: #149a45;
    --green: #1fa84f;
    --green-light: #46bb52;
    --brand-grey: #6b6b6b;
    --text-grey: #666a6d;
    --accent-red: #d9343b;
  }
  * { margin: 0; padding: 0; box-sizing: border-box; }
  html, body { width: 1200px; height: 1023px; overflow: hidden; }
  body {
    background: var(--bg);
    font-family: "Open Sans", sans-serif;
    position: relative;
  }
  .card {
    position: absolute;
    top: 362px;
    width: 520px;
    height: 300px;
    border-radius: 18px;
    overflow: hidden;
    box-shadow: 0 6px 18px rgba(0,0,0,0.14);
  }
  .card--front { left: 50px; background: var(--card-white); }
  .card--back {
    left: 630px;
    background: linear-gradient(135deg, var(--green-light) 0%, var(--green) 55%, var(--green-dark) 100%);
  }

  /* brand lockup */
  .brand { display: flex; align-items: center; gap: 12px; }
  .brand__dot {
    width: 34px; height: 34px; border-radius: 50%;
    background: var(--green);
    flex: none;
  }
  .brand__name {
    font-weight: 600;
    color: var(--brand-grey);
    letter-spacing: 1px;
    white-space: nowrap;
  }
  .brand-rule { height: 2px; background: var(--accent-red); }

  /* front */
  .front__brand { position: absolute; left: 34px; top: 40px; }
  .front__brand .brand__name { font-size: 36px; }
  .front__rule { position: absolute; left: 80px; top: 92px; width: 250px; }
  .front__person { position: absolute; left: 160px; top: 140px; }
  .person__name { font-size: 24px; font-weight: 700; color: var(--green); line-height: 1.1; }
  .person__title { font-size: 12px; color: var(--text-grey); margin-left: 24px; }
  .front__contacts { position: absolute; left: 160px; top: 200px; list-style: none; }
  .contact {
    display: flex; align-items: center; gap: 8px;
    font-size: 12px; color: var(--text-grey); line-height: 20px;
  }
  .contact svg { width: 12px; height: 12px; flex: none; }

  /* back */
  .back__band {
    position: absolute; left: 0; right: 0; top: 92px; height: 116px;
    background: #f4f4f4;
  }
  .back__brand { position: absolute; left: 52px; top: 120px; }
  .back__brand .brand__dot { width: 50px; height: 50px; }
  .back__brand .brand__name { font-size: 46px; }
  .back__rule { position: absolute; left: 116px; top: 186px; width: 340px; }
</style>
</head>
<body>

  <section class="card card--front" aria-label="Business card front">
    <div class="brand front__brand">
      <span class="brand__dot"></span>
      <span class="brand__name">TKR ENERGY</span>
    </div>
    <div class="brand-rule front__rule"></div>

    <div class="front__person">
      <p class="person__name">Your Name</p>
      <p class="person__title">Title</p>
    </div>

    <ul class="front__contacts">
      <li class="contact">
        <svg viewBox="0 0 12 12" aria-hidden="true"><rect x="0.75" y="2.25" width="10.5" height="7.5" fill="none" stroke="var(--green)" stroke-width="1.2"/><path d="M1 2.8 6 6.8 11 2.8" fill="none" stroke="var(--green)" stroke-width="1.2"/></svg>
        info@pelvorpower.co.uk
      </li>
      <li class="contact">
        <svg viewBox="0 0 12 12" aria-hidden="true"><circle cx="6" cy="6" r="5" fill="none" stroke="var(--green)" stroke-width="1.2"/><ellipse cx="6" cy="6" rx="2.2" ry="5" fill="none" stroke="var(--green)" stroke-width="1"/><path d="M1 6h10" stroke="var(--green)" stroke-width="1"/></svg>
        www.pelvorpower.co.uk
      </li>
      <li class="contact">
        <svg viewBox="0 0 12 12" aria-hidden="true"><path d="M6 11.5C3.5 8 2.5 6.3 2.5 4.5a3.5 3.5 0 0 1 7 0c0 1.8-1 3.5-3.5 7z" fill="var(--green)"/><circle cx="6" cy="4.5" r="1.3" fill="#fff"/></svg>
        N7 4QT London, United Kingdom
      </li>
    </ul>
  </section>

  <section class="card card--back" aria-label="Business card back">
    <div class="back__band"></div>
    <div class="brand back__brand">
      <span class="brand__dot"></span>
      <span class="brand__name">TKR ENERGY</span>
    </div>
    <div class="brand-rule back__rule"></div>
  </section>

</body>
</html>
```